依頼概要
■依頼の目的/概要
・電子書籍(自己啓発系)の表紙デザインをお願いします。
・電子書籍は、ソルベリアで販売します。pagoraです。

■本の内容
・初出版本です。
・行き詰った人生を何とかしたいなら、人間関係の苦しみを解消したいなら…。自分の『あり方』を変えることによって、人生がうまくいく方向に動きだすよ ということをお伝えする内容になっています。
・作者の経験が、本の元になっています。
・働く世代や、実際に苦しんでいる当事者、ひきこもりの子どもを持つ親など、幅広く読んでもらいたいです。

■デザイン要望
・明るい未来を感じられるような表紙デザインにしてください。
(底抜けに明るいのは×だけど、悲壮感が見えるのも×)
・人物や、絵が入っている表紙が望ましいです。
(イラスト・写真〇。文字のみのデザインは、×)

■本のタイトル
・本のタイトルは、

毎日が「疲れた…」と感じる君へ、ひとつずつ笑顔が戻ってくる、小さな灯火の地図

です。

・サブキャッチに

~胸のざわめきの理由は〝本音の迷子〟だった~

を入れてください。

■ごあいさつ
・その他、ご不明な点がありましたらお気軽にご質問ください。よろしくお願いします。

■ 選んだ理由

Talkvineをつかって、皆さんからいただいた仮案をアンケートさせていただいたところ、
もっとも「いい」「好き」という評価をいただけたのが、今回選ばせていただいたデザインでした。

なぜよかったのか? と聞いてみたところ
「右下のキャラクターが可愛い」
「見ていると、癒される」
「澄ちゃん(私のこと)らしい」
という意見が、出そろいました。

正直に申しますと、私自身も意外だったのですが
多くの人から「このデザインがいちばん私らしい」と言っていただけるので、気になりはじめ、
今では私自身も気に入っております。

■ 提案者全員のお礼・コメント

本当にありがとうございました。

たった一つのデザインを決めるために、たくさんの方から頂いたデザインを落とさなければならないため、胸を痛めました。
落とすには、あまりにも私好みのデザインがあり過ぎました。

中には私の、初出版の、あまり上手とはいえない文章を丁寧に読んでくれる方もいらっしゃり、とても嬉しかったです。
ありがとうございます。
感謝しています。

また何かの折、お世話になることがあれば、よろしくお願いいたします。

```html
<!DOCTYPE html>
<html lang="ja">
<head>
<meta charset="UTF-8">
<title>小さな灯火の地図 — 表紙</title>
<link rel="stylesheet" href="https://fonts.googleapis.com/css2?family=Noto+Sans+JP:wght@500;900&display=swap">
<style>
  :root {
    --paper: #ffffff;
    --ink: #111111;
    --accent: #f2561d;
    --glow-top: #ffd23a;
    --glow-mid: #ff9a2e;
    --glow-low: #ff4f6a;
    --author: #333333;
  }
  * { margin: 0; padding: 0; box-sizing: border-box; }
  html, body { width: 829px; height: 1200px; overflow: hidden; background: var(--paper); }
  .cover {
    position: relative;
    width: 829px;
    height: 1200px;
    background: var(--paper);
    font-family: "Noto Sans JP", sans-serif;
    overflow: hidden;
  }
  .title {
    position: absolute;
    left: 40px;
    top: 22px;
    font-weight: 900;
    line-height: 1.22;
    letter-spacing: 0.01em;
  }
  .title span { display: block; white-space: nowrap; }
  .title .line-accent { color: var(--accent); }
  .title .line-ink { color: var(--ink); }
  .title .line-1 { font-size: 60px; }
  .title .line-2 { font-size: 60px; }
  .title .line-3 { font-size: 84px; }
  .title .line-4 { font-size: 96px; line-height: 1.15; }
  .author {
    position: absolute;
    left: 78px;
    top: 398px;
    font-size: 26px;
    font-weight: 500;
    color: var(--author);
    letter-spacing: 0.06em;
  }
  .portrait {
    position: absolute;
    left: 150px;
    top: 455px;
    width: 530px;
    height: 560px;
  }
  .subtitle {
    position: absolute;
    left: 0;
    right: 0;
    top: 1005px;
    text-align: center;
    font-weight: 900;
    font-size: 64px;
    line-height: 1.3;
    color: var(--ink);
  }
  .subtitle span { display: block; white-space: nowrap; }
</style>
</head>
<body>
  <main class="cover">
    <h1 class="title">
      <span class="line-1 line-accent">毎日が「疲れた…」と</span>
      <span class="line-2 line-ink">感じる君へ、ひとつずつ</span>
      <span class="line-3 line-accent">笑顔が戻ってくる</span>
      <span class="line-4 line-ink">小さな灯火の地図</span>
    </h1>
    <p class="author">春野澄香</p>
    <svg class="portrait" viewBox="0 0 530 560" role="img" aria-label="明るいグラデーションの円を背に、デニムシャツ姿で笑顔で読者を指さす男性の写真">
      <defs>
        <linearGradient id="glow" x1="0" y1="0" x2="0" y2="1">
          <stop offset="0" stop-color="var(--glow-top)"/>
          <stop offset="0.55" stop-color="var(--glow-mid)"/>
          <stop offset="1" stop-color="var(--glow-low)"/>
        </linearGradient>
      </defs>
      <circle cx="265" cy="285" r="250" fill="url(#glow)"/>
    </svg>
    <p class="subtitle">
      <span>胸のざわめきの理由は</span>
      <span>〝本音の迷子〟だった</span>
    </p>
  </main>
</body>
</html>
```